Harbourline capital partners pty ltd

Hi guys I recently opened a brokerage company. I need a flyer to capture the attention of customers.
I would like something professional and cool at the same time.
My website is harbourcp.com.au
I also attached the current flyer. as you can see it lacks of originality and it isn't cool!!!!
Thank you

Target Market(s)

People between the age of 18-50

Industry/Entity Type

Financial Service

Requirements
Must have
• Mast have features and contents that reflects the website
• harbourcp.com.au
Nice to have
• Open to anything
Should not have
• Not to sure

```html
<!DOCTYPE html>
<html lang="en">
<head>
<meta charset="utf-8">
<title>Harbourline Capital Partners – Flyer</title>
<link href="https://fonts.googleapis.com/css2?family=Open+Sans:wght@400;600;700&display=swap" rel="stylesheet">
<style>
  :root {
    --backdrop: #c4c3c4;
    --paper: #f4f4f4;
    --panel-grey: #e3e3e3;
    --orange: #f08c1a;
    --cyan: #19c0ea;
    --cyan-deep: #0fa3da;
    --blue: #1a84c9;
    --text-dark: #5b5b5b;
    --text-mid: #6e6e6e;
    --white: #ffffff;
  }
  * { box-sizing: border-box; margin: 0; padding: 0; }
  html, body { width: 1200px; height: 900px; overflow: hidden; }
  body {
    background: var(--backdrop);
    font-family: "Open Sans", Arial, sans-serif;
    color: var(--text-dark);
  }
  .flyer {
    position: absolute;
    left: 295px; top: 20px;
    width: 610px; height: 860px;
    background: var(--paper);
    overflow: hidden;
  }
  .flyer-shapes { position: absolute; inset: 0; }

  .hero-photo {
    position: absolute;
    left: 250px; top: 40px;
    width: 360px; height: 200px;
    background: linear-gradient(135deg, #cfc6bd 0%, #a88a74 45%, #6f5a4c 100%);
    clip-path: polygon(0 0, 100% 0, 100% 100%, 22% 100%);
  }
  .brand {
    position: absolute;
    left: 380px; top: 250px;
    width: 220px;
    display: flex; align-items: center; gap: 8px;
  }
  .brand-dot { width: 14px; height: 14px; background: var(--orange); border-radius: 50%; flex: none; }
  .brand-name {
    font-size: 13px; font-weight: 600; color: var(--blue);
    text-transform: uppercase; line-height: 1.2;
  }

  .headline { position: absolute; left: 44px; top: 105px; width: 330px; }
  .headline-lead { font-size: 25px; font-weight: 400; color: var(--text-dark); line-height: 1.1; }
  .headline-accent { font-size: 31px; font-weight: 700; color: var(--orange); line-height: 1.15; }
  .headline-sub {
    margin-top: 10px;
    font-size: 15px; font-weight: 700; color: var(--text-dark); line-height: 1.3;
  }
  .intro {
    position: absolute; left: 44px; top: 255px; width: 300px;
    font-size: 10.5px; line-height: 1.5; color: var(--text-mid);
  }
  .intro strong { color: var(--cyan-deep); font-weight: 700; text-transform: uppercase; }

  .specialty-title {
    position: absolute; left: 44px; top: 372px;
    font-size: 17px; font-weight: 600; color: var(--white);
  }
  .specialty-rule {
    position: absolute; left: 270px; top: 386px; width: 300px; height: 1px;
    background: var(--white);
  }
  .specialty-list {
    position: absolute; left: 36px; top: 408px;
    width: 540px; display: flex; justify-content: space-between;
    list-style: none;
  }
  .specialty-item {
    width: 82px; text-align: center;
    font-size: 10.5px; font-weight: 700; color: var(--white); line-height: 1.2;
  }
  .specialty-icon {
    width: 48px; height: 48px; border-radius: 50%;
    margin: 0 auto 7px;
    background: #f6cd6a;
  }
  .specialty-icon.is-teal { background: #6cc3a4; }
  .specialty-icon.is-coral { background: #ef7a57; }

  .financiers { position: absolute; left: 40px; top: 545px; width: 240px; }
  .section-heading { font-size: 12.5px; font-weight: 700; color: var(--blue); margin-bottom: 4px; }
  .section-copy { font-size: 9px; line-height: 1.45; color: var(--text-dark); margin-bottom: 6px; }
  .bullet-list { list-style: none; font-size: 9px; line-height: 1.45; color: var(--text-dark); }
  .bullet-list li::before { content: "•"; margin: 0 6px 0 4px; }
  .reasons { position: absolute; left: 300px; top: 575px; width: 280px; }
  .reasons .bullet-list li::before { color: var(--cyan); }

  .idea-art {
    position: absolute; left: 190px; top: 650px;
    width: 78px; height: 78px;
    border-radius: 50%;
    background: linear-gradient(135deg, #f6c44a 0%, #1e6ea8 100%);
  }
  .contact-tab {
    position: absolute; left: 270px; top: 690px;
    padding: 6px 16px;
    background: var(--orange); color: var(--white);
    font-size: 15px; font-weight: 700;
  }
  .contact-address {
    position: absolute; left: 262px; top: 745px;
    font-size: 9.5px; line-height: 1.4; color: var(--white);
    display: flex; gap: 6px;
  }
  .contact-lines {
    position: absolute; left: 400px; top: 745px;
    list-style: none; font-size: 9.5px; line-height: 1.9; color: var(--white);
  }
  .contact-lines li { display: flex; align-items: center; gap: 7px; }
  .contact-icon { width: 10px; height: 10px; flex: none; }
</style>
</head>
<body>
  <main class="flyer">
    <svg class="flyer-shapes" width="610" height="860" viewBox="0 0 610 860" aria-hidden="true">
      <defs>
        <linearGradient id="lowerPanel" x1="0" y1="0" x2="0" y2="1">
          <stop offset="0" stop-color="#ececec"/>
          <stop offset="1" stop-color="#cfcfcf"/>
        </linearGradient>
        <linearGradient id="bandFill" x1="0" y1="0" x2="1" y2="0">
          <stop offset="0" stop-color="#14b4e4"/>
          <stop offset="1" stop-color="#2fd0f2"/>
        </linearGradient>
        <linearGradient id="footFill" x1="0" y1="0" x2="1" y2="0">
          <stop offset="0" stop-color="#1a8fd0"/>
          <stop offset="1" stop-color="#2bb6e6"/>
        </linearGradient>
      </defs>
      <!-- upper grey fold -->
      <polygon points="0,90 140,40 250,40 420,360 0,360" fill="var(--panel-grey)"/>
      <polygon points="140,40 250,40 610,360 420,360" fill="#ebebeb"/>
      <!-- orange accent line -->
      <polyline points="20,20 80,75 170,40" fill="none" stroke="var(--orange)" stroke-width="1.5"/>
      <!-- orange block -->
      <polygon points="560,315 610,300 610,400 520,400" fill="var(--orange)"/>
      <!-- lower panel -->
      <rect x="0" y="515" width="610" height="345" fill="url(#lowerPanel)"/>
      <!-- specialty band -->
      <polygon points="0,355 610,370 610,520 0,510" fill="url(#bandFill)"/>
      <polygon points="0,355 300,362 180,510 0,510" fill="#12a9dc" opacity="0.55"/>
      <polygon points="380,364 610,370 610,520 470,516" fill="#4fd8f5" opacity="0.45"/>
      <!-- footer band -->
      <polygon points="180,860 250,730 610,730 610,860" fill="url(#footFill)"/>
      <polygon points="500,860 580,800 610,800 610,860" fill="var(--orange)"/>
    </svg>

    <div class="hero-photo" role="img" aria-label="Photo of a smiling family of four"></div>

    <div class="brand">
      <span class="brand-dot"></span>
      <span class="brand-name">Harbourline Capital Partners Pty Ltd</span>
    </div>

    <header class="headline">
      <p class="headline-lead">We Strive for</p>
      <h1 class="headline-accent">Excellence</h1>
      <p class="headline-sub">Delivering The Right Solution for Our Clients In A Timely and Professional Manner.</p>
    </header>

    <p class="intro"><strong>Harbourline Capital Partners</strong> is a bespoke brokerage firm established by a team of professionals who bring with them over 50 year's combined experience in consulting, finance, negotiation, and executive roles within the finance and automotive industry.</p>

    <h2 class="specialty-title">We specialise in financing</h2>
    <div class="specialty-rule"></div>
    <ul class="specialty-list">
      <li class="specialty-item"><div class="specialty-icon" role="img" aria-label="Car icon"></div>Cars</li>
      <li class="specialty-item"><div class="specialty-icon" role="img" aria-label="Boat icon"></div>Boats</li>
      <li class="specialty-item"><div class="specialty-icon" role="img" aria-label="Caravan icon"></div>Caravans</li>
      <li class="specialty-item"><div class="specialty-icon" role="img" aria-label="Jet ski icon"></div>Jet skis</li>
      <li class="specialty-item"><div class="specialty-icon is-teal" role="img" aria-label="Truck icon"></div>Trucks</li>
      <li class="specialty-item"><div class="specialty-icon is-coral" role="img" aria-label="Excavator icon"></div>Earth moving Equipment</li>
    </ul>

    <section class="financiers">
      <h3 class="section-heading">Our Financiers include</h3>
      <p class="section-copy">We have privileged and specialized access to a wide range of lenders enabling us to tailor solutions which cater to your individual needs. We work with:</p>
      <ul class="bullet-list">
        <li>Southgate Finance</li>
        <li>Kestrel Leasing</li>
        <li>Northway Motor Finance</li>
        <li>Freeport Finance</li>
        <li>Saltbush Asset Finance</li>
        <li>Ridgeline Auto Finance</li>
        <li>Union and General Credit</li>
        <li>Tidewater Marine Finance</li>
        <li>Coastal Bank Finance</li>
      </ul>
    </section>

    <section class="reasons">
      <h3 class="section-heading">Why use us</h3>
      <ul class="bullet-list">
        <li>Low rates</li>
        <li>Access Australia's most trusted lenders</li>
        <li>Quick &amp; easy, same day approvals</li>
        <li>Professional advice</li>
        <li>New, Used, private or dealer sale - the choice is yours</li>
        <li>100% Finance available</li>
      </ul>
    </section>

    <div class="idea-art" role="img" aria-label="Illustration of a head with a lightbulb and dollar sign"></div>

    <div class="contact-tab">Contact Us</div>

    <address class="contact-address">
      <svg class="contact-icon" viewBox="0 0 10 10" aria-hidden="true"><path d="M5 0.5a3.2 3.2 0 0 0-3.2 3.2C1.8 6 5 9.5 5 9.5S8.2 6 8.2 3.7A3.2 3.2 0 0 0 5 0.5z" fill="#fff"/><circle cx="5" cy="3.7" r="1.1" fill="#1a8fd0"/></svg>
      <span>14 Marlow Street<br>Kingsford ACT 2611</span>
    </address>

    <ul class="contact-lines">
      <li><svg class="contact-icon" viewBox="0 0 10 10" aria-hidden="true"><path d="M2 1l2 2-1 1.2c.6 1.3 1.5 2.2 2.8 2.8L7 6l2 2-1.3 1.3C4.5 9 1 5.5.7 2.3z" fill="#fff"/></svg>+61 400 555 018</li>
      <li><svg class="contact-icon" viewBox="0 0 10 10" aria-hidden="true"><rect x="0.5" y="2" width="9" height="6" fill="none" stroke="#fff"/><polyline points="0.5,2 5,5.5 9.5,2" fill="none" stroke="#fff"/></svg>admin@harbourcp.com.au</li>
      <li><svg class="contact-icon" viewBox="0 0 10 10" aria-hidden="true"><circle cx="5" cy="5" r="4.3" fill="none" stroke="#fff"/><line x1="0.7" y1="5" x2="9.3" y2="5" stroke="#fff"/><ellipse cx="5" cy="5" rx="1.8" ry="4.3" fill="none" stroke="#fff"/></svg>www.harbourcp.com.au</li>
    </ul>
  </main>
</body>
</html>
```